Create a Valdossi-looking dashboard for our Quiet Harbor Speedometer that can look similar to my AI-generated dashboard attached, but with: 1) clear borders on all four sides, 2) is created in a way that we can modify the numbers weekly, say maybe you create the graphic that we can inset the excel spreadsheet numbers into, but ideally mixed with the Valdossi look black leather bubble design shown in the dashboard?; 3) uses the exact numbers shown in the attachment; 4) the speedometer on top should have four equal colors of red on left (-1), then yellow (0), then light green (1), then medium green (2); 5) the gauge on the top left should be the graphic that includes 0-100% bar that is currently 33%, and right below that a -20 to +20 bar with the arrow pointing to 11.9%, with color coding similar to the graphic; 6) replace the Valdossi logo in the middle with a similar shaped shield with blue background with the "T" logo with the eagle inside it, like attached

```html
<!DOCTYPE html>
<html lang="en">
<head>
<meta charset="utf-8">
<title>Quiet Harbor Speedometer</title>
<link rel="stylesheet" href="https://fonts.googleapis.com/css2?family=Cinzel:wght@600;700&family=Oswald:wght@400;500;600&family=Libre+Baskerville&display=swap">
<style>
  :root {
    --gold: #d9a93a;
    --gold-light: #f3cf6a;
    --ink: #121212;
    --panel: #1b1b1b;
    --red: #d2261c;
    --orange: #e2551f;
    --yellow: #e8d11f;
    --lime: #a9c93a;
    --green: #5aa83a;
    --stone: #cfc8b8;
    --sand: #ead9ad;
    --white: #f4f1ea;
    --text-dark: #1a1a1a;
  }
  * { box-sizing: border-box; margin: 0; padding: 0; }
  html, body { width: 1200px; height: 800px; overflow: hidden; background: #000; }
  .dashboard {
    position: relative; width: 1200px; height: 800px; overflow: hidden;
    border: 4px solid var(--gold);
    background: var(--ink);
    font-family: "Oswald", sans-serif;
  }
  .dashboard-art { position: absolute; inset: 0; }
  .brand {
    position: absolute; left: 536px; top: 98px; width: 120px;
    text-align: center; color: var(--white);
    font: 600 12px "Oswald", sans-serif; letter-spacing: 1px;
  }
  .brand-dot {
    display: block; width: 16px; height: 16px; margin: 0 auto 4px;
    border-radius: 50%; background: #1d3f8f;
  }
  .title {
    position: absolute; left: 0; width: 1192px; top: 292px;
    text-align: center; color: var(--gold-light);
    font: 700 27px "Cinzel", serif; letter-spacing: 1px;
  }
  .engine-button {
    position: absolute; left: 118px; top: 522px; width: 72px; height: 72px;
    border-radius: 50%; background: radial-gradient(circle at 40% 35%, #e23a30, #8e0d0d);
    border: 3px solid #d8d8d8; box-shadow: 0 0 0 4px #2a2a2a;
    color: var(--white); text-align: center;
    font: 500 11px/1.15 "Oswald", sans-serif; padding-top: 18px;
  }
  .engine-button small { display: block; font-size: 8px; opacity: .8; }

  .grid { position: absolute; display: grid; font-size: 14px; }
  .grid > div {
    display: flex; align-items: center; justify-content: center;
    border: 1px solid #0c0c0c; white-space: nowrap; overflow: hidden;
  }
  .head { color: var(--gold-light); font-size: 14px; background: var(--panel); }
  .gear-cell { justify-content: flex-start !important; padding-left: 4px; color: var(--text-dark); font-weight: 500; }
  .gear-cell b { width: 28px; text-align: right; margin-right: 4px; font-weight: 500; }
  .trend-table { left: 234px; top: 340px; width: 737px;
    grid-template-columns: 232px 281px 224px; grid-template-rows: 20px repeat(4, 20px); }
  .trend-cell { background: linear-gradient(#ddd7c9, #b8b1a2); color: var(--text-dark); font-weight: 600; }
  .change-cell { background: linear-gradient(#ddd7c9, #b8b1a2); color: var(--text-dark); font-family: "Libre Baskerville", serif; font-size: 12px; }
  .change-cell.active { background: linear-gradient(#e8d596, #c9ad62); }

  .stats-table { left: 234px; top: 445px; width: 737px;
    grid-template-columns: 232px 99px 86px 137px 183px; grid-template-rows: 20px repeat(4, 21px) 22px; }
  .stats-table .head { font-size: 12px; }
  .stats-table .head.serif { font-family: "Libre Baskerville", serif; font-size: 10px; color: var(--white); }
  .days-cell { background: var(--sand); color: var(--text-dark); font-weight: 500; }
  .pct-cell { background: linear-gradient(#f1d96a, #d9b53b); color: var(--text-dark); font-weight: 500; }
  .money-cell { background: linear-gradient(#f2e6c4, #d8c594); color: var(--text-dark); font-weight: 500; }
  .money-cell.loss { color: #b0161a; font-weight: 600; }
  .return-cell { background: linear-gradient(#3a2a22, #1a1210); color: var(--white); }
  .return-cell.serif { font-family: "Libre Baskerville", serif; font-size: 11px; background: var(--panel); }
  .return-cell.alert { background: linear-gradient(#e52a1f, #b40f10); }
  .total-label { background: var(--panel); color: var(--gold-light); justify-content: flex-end !important; padding-right: 12px; font-weight: 600; }
  .total-value { background: var(--panel); color: var(--white); }
  .total-note { grid-column: span 3; background: var(--panel); color: var(--white); font-family: "Libre Baskerville", serif; font-size: 10px; }

  .g-boost { background: linear-gradient(90deg, var(--yellow), #d9c21a); }
  .g-accel { background: linear-gradient(90deg, var(--lime), #d6cf2c); }
  .g-brake { background: linear-gradient(90deg, var(--yellow), #e9c51c); }
  .g-reverse { background: linear-gradient(90deg, var(--red), #e0442c); }
  .s-boost { background: linear-gradient(90deg, var(--green), #a8c83a); font-size: 17px; font-weight: 600 !important; }
  .s-accel { background: linear-gradient(90deg, #d5c91f, var(--yellow)); }
  .s-brake { background: linear-gradient(90deg, var(--orange), #e9702a); }
  .s-reverse { background: linear-gradient(90deg, var(--red), #e2331f); }

  .period {
    position: absolute; top: 584px; left: 0; width: 1192px; height: 22px;
    color: var(--white); font-family: "Libre Baskerville", serif;
  }
  .period-total { position: absolute; left: 508px; top: 0; color: var(--stone); font-family: "Cinzel", serif; font-size: 17px; line-height: 22px; letter-spacing: 2px; }
  .period-range { position: absolute; left: 752px; top: 0; font-size: 13px; line-height: 22px; }

  .signal-table { left: 261px; top: 614px; width: 675px;
    grid-template-columns: 230px 223px 222px; grid-template-rows: 28px repeat(3, 25px) 32px; font-size: 15px; }
  .signal-table > div { border: 1px solid rgba(0,0,0,.35); }
  .bull { background: linear-gradient(90deg, #2f7a2e, #6fb43e); color: var(--text-dark); }
  .bullish { background: linear-gradient(90deg, #e0cc1a, #ecd832); color: var(--text-dark); }
  .bullish.warn { color: #c2261c; }
  .bearish { background: linear-gradient(90deg, #c21914, #d93321); color: #f3d9cf; }
  .sig-head { font-size: 17px; }
  .bull.sig-head { background: linear-gradient(90deg, #1f5a23, #3c8a34); color: var(--white); }
  .bullish.sig-head { background: linear-gradient(90deg, #3b3710, #4b4413); color: var(--yellow); }
  .bearish.sig-head { background: linear-gradient(90deg, #4a0d0b, #6b1410); color: var(--white); }
  .sig-last { background: #1d2a17; color: #98c75c; }
  .sig-last.mid { background: #2c2a12; color: #e0cf6a; }
  .sig-last.bad { background: #3a0f0c; color: #f1d6a0; font-family: "Libre Baskerville", serif; font-size: 17px; }
  .sig-last.bad small { font-size: 10px; margin-left: 6px; }
  .footnote {
    position: absolute; left: 315px; top: 760px; width: 570px;
    color: #a9a9a9; font-size: 8px; line-height: 10px; font-family: "Oswald", sans-serif;
  }
</style>
</head>
<body>
<main class="dashboard">
  <svg class="dashboard-art" width="1192" height="792" viewBox="0 0 1192 792" aria-hidden="true">
    <defs>
      <radialGradient id="leather" cx="50%" cy="40%" r="70%">
        <stop offset="0" stop-color="#c4252a"/>
        <stop offset="1" stop-color="#5e080c"/>
      </radialGradient>
      <linearGradient id="carbon" x1="0" y1="0" x2="0" y2="1">
        <stop offset="0" stop-color="#2a2a2a"/>
        <stop offset="1" stop-color="#141414"/>
      </linearGradient>
      <radialGradient id="dial" cx="50%" cy="60%" r="60%">
        <stop offset="0" stop-color="#2b2b2b"/>
        <stop offset="1" stop-color="#0c0c0c"/>
      </radialGradient>
      <linearGradient id="trendBar" x1="0" y1="0" x2="1" y2="0">
        <stop offset="0" stop-color="#d02b1d"/>
        <stop offset=".5" stop-color="#e8d11f"/>
        <stop offset="1" stop-color="#3f9a3a"/>
      </linearGradient>
    </defs>
    <rect width="1192" height="792" fill="#0e0e0e"/>
    <!-- leather surfaces -->
    <path d="M0 150 Q150 110 300 150 L300 800 L0 800 Z" fill="url(#leather)"/>
    <path d="M892 150 Q1042 110 1192 150 L1192 800 L892 800 Z" fill="url(#leather)"/>
    <path d="M100 200 Q300 90 470 60 Q596 15 722 60 Q892 90 1092 200 L1060 240 Q900 150 722 120 L470 120 Q292 150 132 240 Z" fill="url(#leather)"/>
    <path d="M90 410 Q100 380 140 380 L210 380 L215 690 Q150 700 100 650 Z" fill="#8f1116"/>
    <path d="M990 380 L1060 380 Q1100 390 1100 430 L1100 650 Q1040 700 985 690 Z" fill="#8f1116"/>
    <!-- vent openings -->
    <ellipse cx="12" cy="280" rx="50" ry="80" fill="#161616"/>
    <ellipse cx="1180" cy="280" rx="50" ry="80" fill="#161616"/>
    <rect x="1080" y="560" width="112" height="110" rx="40" fill="#141414"/>
    <!-- instrument binnacle -->
    <path d="M150 240 Q300 150 450 150 L742 150 Q892 150 1042 240 L1030 360 Q596 330 162 360 Z" fill="url(#carbon)"/>
    <path d="M225 330 Q596 300 967 330 L977 578 L215 578 Z" fill="#1a1a1a" stroke="#555" stroke-width="3"/>
    <path d="M250 608 L942 608 L952 792 L240 792 Z" fill="#121212" stroke="#444" stroke-width="3"/>
    <!-- red indicator lights -->
    <circle cx="385" cy="172" r="7" fill="#ff3b30"/>
    <circle cx="808" cy="172" r="7" fill="#ff3b30"/>

    <!-- center gauge: four equal sectors -->
    <g transform="translate(596 246)">
      <circle r="190" fill="#0b0b0b" stroke="#6b6b6b" stroke-width="4"/>
      <path d="M-178 0 A178 178 0 0 1 -125.9 -125.9 L0 0 Z" fill="#d8321f"/>
      <path d="M-125.9 -125.9 A178 178 0 0 1 0 -178 L0 0 Z" fill="#e2cc22"/>
      <path d="M0 -178 A178 178 0 0 1 125.9 -125.9 L0 0 Z" fill="#6fb43e"/>
      <path d="M125.9 -125.9 A178 178 0 0 1 178 0 L0 0 Z" fill="#3f8a35"/>
      <path d="M-178 0 A178 178 0 0 1 178 0" fill="none" stroke="#9fd65b" stroke-width="4"/>
      <path d="M-169 -55 A178 178 0 0 1 -125.9 -125.9" fill="none" stroke="#f39a1a" stroke-width="8"/>
      <circle r="66" fill="none" stroke="rgba(0,0,0,.18)" stroke-width="2"/>
      <circle r="118" fill="none" stroke="rgba(0,0,0,.15)" stroke-width="2"/>
      <rect x="-195" y="0" width="390" height="60" fill="#1a1a1a"/>
      <path d="M-52 0 A52 52 0 0 1 52 0 Z" fill="#222" stroke="#888" stroke-width="3"/>
      <path d="M-6 -6 L82 -128 L6 6 Z" fill="#e9b93a"/>
      <circle r="18" fill="#e9b93a" stroke="#8c6414" stroke-width="2"/>
    </g>

    <!-- left gauge: 0-100% dial with -20/+20 trend bar -->
    <g transform="translate(257 240)" font-family="Oswald, sans-serif">
      <circle r="96" fill="#3a3a3a"/>
      <circle r="89" fill="url(#dial)"/>
      <path d="M-68 0 A68 68 0 0 1 0 -68" fill="none" stroke="#2f9a3a" stroke-width="7"/>
      <path d="M0 -68 A68 68 0 0 1 55 -40" fill="none" stroke="#e2a620" stroke-width="7"/>
      <path d="M55 -40 A68 68 0 0 1 68 0" fill="none" stroke="#d02b1d" stroke-width="7"/>
      <g stroke="#eee" stroke-width="2">
        <line x1="-78" y1="0" x2="-86" y2="0"/>
        <line x1="-55" y1="-55" x2="-61" y2="-61"/>
        <line x1="0" y1="-78" x2="0" y2="-86"/>
        <line x1="55" y1="-55" x2="61" y2="-61"/>
        <line x1="78" y1="0" x2="86" y2="0"/>
      </g>
      <g fill="#eee" font-size="11" text-anchor="middle">
        <text x="-56" y="14">0%</text>
        <text x="0" y="-48">50%</text>
        <text x="54" y="14">100%</text>
      </g>
      <line x1="0" y1="0" x2="-31" y2="-53" stroke="#f0c23a" stroke-width="4" stroke-linecap="round"/>
      <circle r="8" fill="#222" stroke="#888" stroke-width="2"/>
      <text x="0" y="24" fill="#f3cf6a" font-size="13" font-weight="600" text-anchor="middle">33%</text>
      <rect x="-60" y="38" width="120" height="9" rx="2" fill="url(#trendBar)"/>
      <line x1="0" y1="36" x2="0" y2="49" stroke="#111" stroke-width="1.5"/>
      <path d="M35.7 36 L30.7 28 L40.7 28 Z" fill="#f4f1ea"/>
      <g fill="#eee" font-size="10" text-anchor="middle">
        <text x="-60" y="60">-20</text>
        <text x="0" y="60">0</text>
        <text x="60" y="60">+20</text>
      </g>
      <text x="36" y="24" fill="#9fd65b" font-size="11" font-weight="600" text-anchor="middle">11.9%</text>
    </g>

    <!-- right gauge -->
    <g transform="translate(940 240)">
      <circle r="96" fill="#3a3a3a"/>
      <circle r="89" fill="url(#dial)"/>
      <g stroke="#eee" stroke-width="2">
        <line x1="-66" y1="38" x2="-77" y2="44"/><line x1="-74" y1="5" x2="-85" y2="5"/>
        <line x1="-66" y1="-34" x2="-77" y2="-40"/><line x1="-37" y1="-66" x2="-43" y2="-77"/>
        <line x1="0" y1="-74" x2="0" y2="-85"/><line x1="37" y1="-66" x2="43" y2="-77"/>
      </g>
      <g stroke="#e33" stroke-width="3">
        <line x1="66" y1="-34" x2="77" y2="-40"/><line x1="74" y1="5" x2="85" y2="5"/>
        <line x1="66" y1="38" x2="77" y2="44"/>
      </g>
      <g fill="#eee" font-family="Oswald, sans-serif" font-size="14" text-anchor="middle">
        <text x="-50" y="58" font-size="17">150</text><text x="-50" y="-14">210</text>
        <text x="-16" y="-46">280</text><text x="20" y="-46">290</text>
        <text x="46" y="-14">250</text><text x="52" y="58">250</text>
      </g>
      <line x1="0" y1="0" x2="-40" y2="24" stroke="#e33" stroke-width="5"/>
      <line x1="0" y1="0" x2="36" y2="-18" stroke="#e33" stroke-width="3"/>
      <circle r="13" fill="#222" stroke="#666" stroke-width="2"/>
    </g>
  </svg>

  <div class="brand"><span class="brand-dot"></span>QUIET HARBOR</div>
  <h1 class="title">QUIET HARBOR SPEEDOMETER</h1>

  <div class="engine-button">ENGINE<br>START<small>STOP</small></div>

  <section class="grid trend-table" aria-label="Current trend">
    <div class="head">GEAR</div><div class="head">CURRENT TREND</div><div class="head">LAST TREND CHANGE</div>
    <div class="gear-cell g-boost"><b>2</b>TURBO BOOST</div><div class="trend-cell">BULL</div><div class="change-cell active">Friday, August 15, 2014</div>
    <div class="gear-cell g-accel"><b>1</b>ACCELERATOR PEDAL</div><div class="trend-cell">BULLISH</div><div class="change-cell"></div>
    <div class="gear-cell g-brake"><b>0</b>BRAKES</div><div class="trend-cell">BEARISH</div><div class="change-cell"></div>
    <div class="gear-cell g-reverse"><b>-1</b>REVERSE</div><div class="trend-cell">BEAR</div><div class="change-cell"></div>
  </section>

  <section class="grid stats-table" aria-label="Gear statistics">
    <div class="head">GEAR</div><div class="head">TOTAL DAYS</div><div class="head">PERCENT</div><div class="head">$100,000 INVESTED</div><div class="head serif">Meridian 500 Annualized Return</div>
    <div class="gear-cell s-boost"><b>2</b>TURBO BOOST</div><div class="days-cell">3564</div><div class="pct-cell">69.11%</div><div class="money-cell">$779,158</div><div class="return-cell serif">GAIN/LOSS, 15.08%</div>
    <div class="gear-cell s-accel"><b>1</b>ACCELERATOR PEDAL</div><div class="days-cell">547</div><div class="pct-cell">10.62%</div><div class="money-cell">$249,993</div><div class="return-cell">0.84%</div>
    <div class="gear-cell s-brake"><b>0</b>BRAKES</div><div class="days-cell">937</div><div class="pct-cell">18.17%</div><div class="money-cell loss">$82,111</div><div class="return-cell">-8.16%</div>
    <div class="gear-cell s-reverse"><b>-1</b>REVERSE</div><div class="days-cell">129</div><div class="pct-cell">2.49%</div><div class="money-cell loss">$55,344</div><div class="return-cell alert">20.53%</div>
    <div class="total-label">TOTAL:</div><div class="total-value">5137</div><div class="total-note">Meridian 500 · MRD · Annualized averages Drawdown</div>
  </section>

  <div class="period">
    <span class="period-total">TOTAL: 5157</span>
    <span class="period-range"><b>07/05</b>/2005 TO 13/01/2024</span>
  </div>

  <section class="grid signal-table" aria-label="Gear signals">
    <div class="bull sig-head">TURBO BOOST (BULL)</div><div class="bullish sig-head">ACCELERATOR (BULLISH)</div><div class="bearish sig-head">BRAKES (BEARISH)</div>
    <div class="bull">DELTA/V*</div><div class="bullish">CALENDAR +</div><div class="bearish">NEGATIVE</div>
    <div class="bull">CALENDAR +</div><div class="bullish">TURBO +</div><div class="bearish">NEGATIVE</div>
    <div class="bull">TURBO +</div><div class="bullish warn">TURBO -</div><div class="bearish">NEGATIVE</div>
    <div class="sig-last">REVERSE -</div><div class="sig-last mid">REVERSE -</div><div class="sig-last bad">GOLD<small>ASTRONOUT +</small></div>
  </section>

  <p class="footnote">The Meridian 500 is an unmanaged market index; returns shown are hypothetical, exclude fees and taxes, and do not guarantee future results.<br>Data updated weekly by the research desk from model signals.</p>
</main>
</body>
</html>
```